Business Card Design

Attached is the logo of the store.

Information needed on the business card:

www.brookvale17vino.com
info@brookvale17vino.com
412 Harlow St NY, NY 10027
Tel:(646) 472-3958

Store Hours
Mon-Sat Noon-10pm
Sun Noon-8pm

Free Deliveries

Industry/Entity Type

Business

Contact Information for Business Card

Brookvale 17 Wine & Spirits

```html
<!DOCTYPE html>
<html lang="en">
<head>
<meta charset="utf-8">
<title>Brookvale 17 Wine &amp; Spirits — Business Card</title>
<link rel="stylesheet" href="https://fonts.googleapis.com/css2?family=Source+Sans+3:wght@400;600&display=swap">
<style>
  :root {
    --card-charcoal: #2c292a;
    --card-shadow: rgba(0, 0, 0, 0.28);
    --brand-red: #e1364e;
    --ink-white: #ffffff;
    --page-bg: #ffffff;
  }
  * { box-sizing: border-box; margin: 0; padding: 0; }
  html, body { width: 1200px; height: 800px; overflow: hidden; background: var(--page-bg); }
  body { font-family: "Source Sans 3", "Myriad Pro", Arial, sans-serif; color: var(--ink-white); }

  .canvas { position: relative; width: 1200px; height: 800px; }

  .card {
    position: absolute;
    background: var(--card-charcoal);
    box-shadow: 0 6px 14px var(--card-shadow);
    overflow: hidden;
  }
  .card--back  { left: 200px; top: 40px;  width: 780px; height: 560px; }
  .card--front { left: 250px; top: 320px; width: 740px; height: 440px; }

  .brand {
    position: absolute;
    text-align: center;
    font-weight: 400;
    color: var(--ink-white);
    line-height: 1;
    letter-spacing: 0.5px;
  }
  .card--back .brand  { left: 0; right: 0; top: 120px; font-size: 68px; }
  .card--front .brand { left: 0; right: 0; top: 70px;  font-size: 64px; }
  .brand__tag { display: block; margin-top: 10px; font-size: 0.46em; letter-spacing: 1px; }

  .info-band {
    position: absolute;
    left: 0; right: 0; bottom: 0;
    height: 166px;
    background: var(--brand-red);
    display: flex;
    justify-content: space-between;
    padding: 14px 70px 0 48px;
    font-size: 21px;
    line-height: 26px;
  }
  .contact, .hours { list-style: none; }
  .hours { width: 220px; }
  .hours__delivery { margin-top: 8px; font-size: 25px; font-weight: 600; }
</style>
</head>
<body>
  <main class="canvas">
    <section class="card card--back" aria-label="Business card back">
      <div class="brand">Brookvale 17<span class="brand__tag">Wine &amp; Spirits</span></div>
    </section>

    <section class="card card--front" aria-label="Business card front">
      <div class="brand">Brookvale 17<span class="brand__tag">Wine &amp; Spirits</span></div>
      <div class="info-band">
        <ul class="contact">
          <li>www.brookvale17vino.com</li>
          <li>info@brookvale17vino.com</li>
          <li>412 Harlow St NY, NY 10027</li>
          <li>Tel:(646) 472-3958</li>
        </ul>
        <ul class="hours">
          <li>Store Hours</li>
          <li>Mon-Sat Noon-10pm</li>
          <li>Sun Noon-8pm</li>
          <li class="hours__delivery">Free Deliveries</li>
        </ul>
      </div>
    </section>
  </main>
</body>
</html>
```